Vellorin - Business Cards for a new venture

create business card for a startup classified business dealing in construction materials, the cards need to have a professional look but modern, more serious than playful, one of the samples must include the official font (attached), please explore using the official colors in the company's logo

Target Market(s)

Energy sector

Contact Information for Business Card

Font styles to use
Other font styles liked:
• suissnord

Requirements
Must have
• corporate colors (in logo attached)
Nice to have
• Official font (in one of the samples) font is : suissnord
Should not have
• Cartoonish look

```html
<!DOCTYPE html>
<html lang="en">
<head>
<meta charset="utf-8">
<title>Vellorin Business Card</title>
<link rel="stylesheet" href="https://fonts.googleapis.com/css2?family=Saira:wght@400;500;600&family=Michroma&display=swap">
<style>
  :root {
    --stage: #2b2d30;
    --brand-blue: #134a7c;
    --ink-blue: #0f3f73;
    --steel: #9a9ea4;
    --paper: #ffffff;
    --icon-grey: #a3a6aa;
  }
  * { box-sizing: border-box; margin: 0; padding: 0; }
  html, body { width: 1200px; height: 902px; overflow: hidden; }
  body {
    background: var(--stage);
    display: flex;
    align-items: center;
    justify-content: center;
    gap: 40px;
    font-family: "Saira", sans-serif;
  }
  .card {
    width: 540px;
    height: 309px;
    border-radius: 22px;
    position: relative;
    overflow: hidden;
  }
  .card--back {
    background: var(--brand-blue);
    display: flex;
    align-items: center;
    justify-content: center;
  }
  .wordmark {
    font-family: "Saira", sans-serif;
    font-weight: 500;
    color: var(--steel);
    letter-spacing: 0.22em;
    text-transform: uppercase;
    line-height: 1;
  }
  .card--back .wordmark { font-size: 34px; }
  .card--front { background: var(--paper); }
  .card--front .wordmark {
    position: absolute;
    right: 70px;
    top: 72px;
    font-size: 30px;
  }
  .divider {
    position: absolute;
    left: 200px;
    right: 26px;
    top: 150px;
    height: 1.5px;
    background: var(--ink-blue);
  }
  .holder {
    position: absolute;
    left: 34px;
    top: 124px;
  }
  .holder__name {
    font-family: "Michroma", sans-serif;
    color: var(--ink-blue);
    font-size: 19px;
    letter-spacing: 0.02em;
    line-height: 1;
    text-transform: uppercase;
  }
  .holder__role {
    color: var(--steel);
    font-size: 12.5px;
    letter-spacing: 0.14em;
    text-transform: uppercase;
    margin-top: 5px;
  }
  .holder__rule {
    width: 160px;
    height: 1.5px;
    background: var(--ink-blue);
    margin-top: 8px;
  }
  .contacts {
    position: absolute;
    left: 34px;
    top: 200px;
    list-style: none;
  }
  .contacts li {
    display: flex;
    align-items: center;
    gap: 10px;
    color: var(--ink-blue);
    font-size: 15px;
    font-weight: 500;
    letter-spacing: 0.04em;
    height: 26px;
  }
  .contacts svg { width: 18px; height: 18px; flex: none; }
  .address {
    position: absolute;
    right: 30px;
    top: 160px;
    text-align: right;
    color: var(--ink-blue);
    font-size: 14px;
    font-weight: 500;
    letter-spacing: 0.04em;
    line-height: 1.4;
  }
</style>
</head>
<body>
  <section class="card card--back" aria-label="Card back">
    <span class="wordmark">Vellorin</span>
  </section>

  <section class="card card--front" aria-label="Card front">
    <span class="wordmark">Vellorin</span>
    <div class="divider"></div>

    <div class="holder">
      <p class="holder__name">Daniel Harlow</p>
      <p class="holder__role">Managing Director</p>
      <div class="holder__rule"></div>
    </div>

    <ul class="contacts">
      <li>
        <svg viewBox="0 0 18 18" aria-hidden="true"><circle cx="9" cy="9" r="9" fill="var(--icon-grey)"/><path d="M6 5.2l1.6-.4 1 2.2-1 .8c.4 1 1.2 1.8 2.2 2.2l.8-1 2.2 1-.4 1.6c-3.4.2-6.6-3-6.4-6.4z" fill="#fff"/></svg>
        +612 4870 1526
      </li>
      <li>
        <svg viewBox="0 0 18 18" aria-hidden="true"><circle cx="9" cy="9" r="9" fill="var(--icon-grey)"/><rect x="6.4" y="4.2" width="5.2" height="9.6" rx="1" fill="#fff"/><rect x="7.2" y="5.2" width="3.6" height="6.4" fill="var(--icon-grey)"/></svg>
        +612 4870 3391
      </li>
      <li>
        <svg viewBox="0 0 18 18" aria-hidden="true"><circle cx="9" cy="9" r="9" fill="var(--icon-grey)"/><rect x="4.6" y="5.8" width="8.8" height="6.4" fill="#fff"/><path d="M4.8 6l4.2 3.4L13.2 6" fill="none" stroke="var(--icon-grey)" stroke-width="0.9"/></svg>
        info@vellorin.com
      </li>
    </ul>

    <p class="address">1870 Ridgeway Commerce Drive<br>Fenton, MO 63026</p>
  </section>
</body>
</html>
```